Dietary supplement package design

We need a design for a range of dietary supplements mentioned below. The colors can be derived from the attached company logo and the package is a plastic bottle for medicines use (attached is a sample). All products will have the same package design and color with a permissible slight change to product name and associated picture/artwork (if any). Please avoid using pictures of humans or animals. We expect to see a label with three panels:
1. Left panel containing instructions, warnings and other information.
2. Front panel containing products name and its unique look
3. Right panel containing nutrient/ingredient information table and address.
The label will dual language (Arabic/English) and we have no issue to use special colors, i.e. UV, gold or silver.
Products names are:
1. Ginkgo biloba
2. Slimming formula
3. Fat Absorber
4. Glutathione
5. Royal Jelly
6. Vitamin D
Reason: Allow designers to provide more suggestions
Target Market(s)
Consumers and health care professionals
Industry/Entity Type
Healthcare
Look and feel

```html
<!DOCTYPE html>
<html lang="en">
<head>
<meta charset="utf-8">
<title>Vantera Supplement Labels</title>
<link href="https://fonts.googleapis.com/css2?family=Fredoka:wght@500&family=Nunito:wght@700;800&family=Roboto+Condensed:wght@400&family=Crimson+Pro:ital,wght@1,500&display=swap" rel="stylesheet">
<style>
  :root {
    --bg: #efefef;
    --label-white: #ffffff;
    --blue: #2a9fd8;
    --orange: #f5a623;
    --green: #2e9a3a;
    --leaf-light: #d6edc9;
    --leaf-mid: #a9d78f;
    --comb-light: #fbe39a;
    --comb-mid: #f3c443;
    --ink: #262626;
  }
  * { box-sizing: border-box; margin: 0; padding: 0; }
  html, body {
    width: 1200px;
    height: 1200px;
    overflow: hidden;
    background: var(--bg);
  }
  .canvas {
    position: relative;
    width: 1200px;
    height: 1200px;
    display: flex;
    justify-content: center;
    align-items: center;
    gap: 80px;
  }
  .label {
    position: relative;
    width: 460px;
    height: 560px;
    filter: drop-shadow(0 6px 18px rgba(0,0,0,0.08));
  }
  .label-shapes {
    position: absolute;
    inset: 0;
    width: 460px;
    height: 560px;
  }
  .artwork {
    position: absolute;
  }
  .artwork--ginkgo {
    left: 24px;
    top: 330px;
    width: 200px;
    height: 178px;
    border-radius: 40% 60% 20% 10%;
    background: radial-gradient(ellipse at 45% 55%, var(--leaf-mid), var(--leaf-light) 60%, rgba(214,237,201,0) 100%);
  }
  .artwork--honeycomb {
    left: 0;
    top: 250px;
    width: 150px;
    height: 250px;
    border-radius: 0 50% 50% 0;
    background: radial-gradient(ellipse at 40% 50%, var(--comb-mid), var(--comb-light) 60%, rgba(251,227,154,0) 100%);
  }
  .brand {
    position: absolute;
    top: 46px;
    left: 0;
    right: 0;
    text-align: center;
  }
  .brand-name {
    display: inline-flex;
    align-items: center;
    gap: 12px;
    font-family: "Nunito", sans-serif;
    font-weight: 800;
    font-size: 54px;
    line-height: 1;
    color: var(--blue);
  }
  .brand-mark {
    width: 22px;
    height: 22px;
    background: var(--blue);
  }
  .brand-sub {
    margin-top: 6px;
    font-family: "Nunito", sans-serif;
    font-weight: 700;
    font-size: 14px;
    color: var(--green);
  }
  .product {
    position: absolute;
    right: 34px;
    top: 220px;
    text-align: right;
  }
  .product-name {
    font-family: "Fredoka", sans-serif;
    font-weight: 500;
    font-size: 62px;
    line-height: 1;
    letter-spacing: -1px;
  }
  .product-name--ginkgo { color: var(--green); }
  .product-name--jelly { color: var(--orange); }
  .product-variant {
    margin-top: 8px;
    font-family: "Crimson Pro", serif;
    font-style: italic;
    font-weight: 500;
    font-size: 30px;
    color: var(--ink);
  }
  .claims {
    position: absolute;
    right: 34px;
    top: 388px;
    text-align: right;
    font-family: "Roboto Condensed", sans-serif;
    font-size: 21px;
    line-height: 1.35;
    color: var(--ink);
    list-style: none;
  }
  .count {
    position: absolute;
    right: 34px;
    top: 452px;
    font-family: "Fredoka", sans-serif;
    font-weight: 500;
    font-size: 27px;
    color: var(--ink);
  }
  .footer-band {
    position: absolute;
    left: 0;
    right: 0;
    bottom: 10px;
    text-align: center;
    font-family: "Roboto Condensed", sans-serif;
    font-size: 21px;
    color: var(--label-white);
  }
</style>
</head>
<body>
<main class="canvas">

  <section class="label label--ginkgo">
    <svg class="label-shapes" viewBox="0 0 460 560" aria-hidden="true">
      <defs>
        <clipPath id="ginkgo-outline"><rect width="460" height="560" rx="28"/></clipPath>
      </defs>
      <g clip-path="url(#ginkgo-outline)">
        <rect width="460" height="560" fill="var(--label-white)"/>
        <polygon points="0,0 120,0 0,130" fill="var(--blue)"/>
        <polygon points="340,0 460,0 460,130" fill="var(--orange)"/>
        <rect x="0" y="130" width="20" height="380" fill="var(--green)"/>
        <rect x="440" y="130" width="20" height="380" fill="var(--green)"/>
        <rect x="0" y="510" width="460" height="50" fill="var(--green)"/>
        <polygon points="370,560 460,560 460,460" fill="var(--blue)"/>
      </g>
    </svg>
    <div class="artwork artwork--ginkgo" role="img" aria-label="Line drawing of a ginkgo branch with fan-shaped leaves"></div>
    <header class="brand">
      <div class="brand-name"><span class="brand-mark"></span>Vantera</div>
      <div class="brand-sub">VitaMedica &amp; Supplies</div>
    </header>
    <div class="product">
      <h1 class="product-name product-name--ginkgo">Ginkgo Biloba</h1>
      <p class="product-variant">Leaf Extract</p>
    </div>
    <ul class="claims">
      <li>Brain Functions</li>
      <li>Antioxidant System</li>
    </ul>
    <p class="count" style="top:458px">60 caps</p>
    <p class="footer-band">Natural Dietary Supplement</p>
  </section>

  <section class="label label--jelly">
    <svg class="label-shapes" viewBox="0 0 460 560" aria-hidden="true">
      <defs>
        <clipPath id="jelly-outline"><rect width="460" height="560" rx="28"/></clipPath>
      </defs>
      <g clip-path="url(#jelly-outline)">
        <rect width="460" height="560" fill="var(--label-white)"/>
        <polygon points="0,0 120,0 0,130" fill="var(--blue)"/>
        <polygon points="340,0 460,0 460,130" fill="var(--orange)"/>
        <rect x="0" y="130" width="20" height="380" fill="var(--orange)"/>
        <rect x="440" y="130" width="20" height="380" fill="var(--orange)"/>
        <rect x="0" y="510" width="460" height="50" fill="var(--orange)"/>
        <polygon points="0,450 0,560 100,560" fill="var(--green)"/>
        <polygon points="370,560 460,560 460,460" fill="var(--blue)"/>
      </g>
    </svg>
    <div class="artwork artwork--honeycomb" role="img" aria-label="Golden honeycomb cells curving down the left edge"></div>
    <header class="brand">
      <div class="brand-name"><span class="brand-mark"></span>Vantera</div>
      <div class="brand-sub">VitaMedica &amp; Supplies</div>
    </header>
    <div class="product">
      <h1 class="product-name product-name--jelly">Royal Jelly</h1>
      <p class="product-variant">Golden Hive</p>
    </div>
    <ul class="claims">
      <li>Support Cardiovascular Health</li>
      <li>Immune System Function</li>
    </ul>
    <p class="count" style="top:458px">60 caps</p>
    <p class="footer-band">Natural Dietary Supplement</p>
  </section>

</main>
</body>
</html>
```